Business card with logo and words.

Colours: aqua and white (but open to suggestions).
Double sided card ok.
Need to convey competence, calmness, listening skills
Words:
Quiet Harbour Care Planning
Rhoda Pemberton
RN, RM, MVRNB, Grad Dip Gr & Pall Care Couns, Grad Cert Pall Care in Aged Care
quietharbourcp@fernmail.example

```html
<!DOCTYPE html>
<html lang="en">
<head>
<meta charset="utf-8">
<title>Quiet Harbour Care Planning – Business Card</title>
<link rel="stylesheet" href="https://fonts.googleapis.com/css2?family=PT+Serif:ital,wght@1,400&family=Ubuntu:wght@400&display=swap">
<style>
  :root {
    --page-bg: #f4f5f7;
    --card-aqua: #00bdf2;
    --card-white: #ffffff;
    --ink-navy: #1f2f3a;
    --title-shadow: rgba(0, 50, 80, 0.45);
  }
  * { box-sizing: border-box; margin: 0; padding: 0; }
  html, body {
    width: 1200px;
    height: 1021px;
    overflow: hidden;
    background: var(--page-bg);
  }
  .sheet {
    position: relative;
    width: 1200px;
    height: 1021px;
  }
  .card {
    position: absolute;
    top: 129px;
    width: 358px;
    height: 678px;
    background: var(--card-aqua);
    color: var(--card-white);
    text-align: center;
  }
  .card--front { left: 168px; }
  .card--back { left: 648px; }

  .brand {
    position: absolute;
    top: 110px;
    left: 0;
    width: 100%;
    height: 150px;
    display: flex;
    align-items: center;
    justify-content: center;
    gap: 18px;
  }
  .brand__dot {
    flex: none;
    width: 30px;
    height: 30px;
    border-radius: 50%;
    background: var(--card-white);
  }
  .brand__name {
    font-family: "Ubuntu", sans-serif;
    font-weight: 400;
    font-size: 50px;
    line-height: 1.08;
    text-align: left;
    color: var(--card-white);
  }

  .headline {
    position: absolute;
    top: 392px;
    left: 0;
    width: 100%;
    font-family: "PT Serif", serif;
    font-style: italic;
    font-weight: 400;
    font-size: 58px;
    line-height: 80px;
    text-shadow: 2px 3px 3px var(--title-shadow);
  }

  .person {
    position: absolute;
    top: 392px;
    left: 0;
    width: 100%;
  }
  .person__name {
    font-family: "PT Serif", serif;
    font-style: italic;
    font-weight: 400;
    font-size: 44px;
    line-height: 64px;
    white-space: nowrap;
    text-shadow: 2px 3px 3px var(--title-shadow);
  }
  .person__credentials {
    margin-top: 30px;
    font-family: "Ubuntu", sans-serif;
    font-weight: 400;
    font-size: 18px;
    line-height: 25px;
    color: var(--ink-navy);
  }

  .contact-email {
    position: absolute;
    bottom: 12px;
    right: 26px;
    font-family: "Ubuntu", sans-serif;
    font-weight: 400;
    font-size: 18px;
    color: var(--ink-navy);
  }
</style>
</head>
<body>
<main class="sheet">
  <section class="card card--front" aria-label="Card front">
    <div class="brand">
      <span class="brand__dot"></span>
      <span class="brand__name">Quiet<br>Harbour</span>
    </div>
    <h1 class="headline">Care<br>Planning</h1>
    <p class="contact-email">quietharbourcp@fernmail.example</p>
  </section>

  <section class="card card--back" aria-label="Card back">
    <div class="brand">
      <span class="brand__dot"></span>
      <span class="brand__name">Quiet<br>Harbour</span>
    </div>
    <div class="person">
      <h2 class="person__name">Rhoda Pemberton</h2>
      <p class="person__credentials">
        RN, RM, MVRNB<br>
        Grad Dip Gr &amp; Pall Care Couns<br>
        Grad Cert Pall Care in Aged Care
      </p>
    </div>
    <p class="contact-email">quietharbourcp@fernmail.example</p>
  </section>
</main>
</body>
</html>
```